Thornbury Lettings Managment Ltd website

Need a website To inform people/clients of the services we provide. 5 pages total with a local feel. Bristol, UK. I have logo artwork already is like the look based on
incorporate the artwork attached for theme, feel and colours fonts info etc

To best describe the business have a brief look at www.fernwickhomes.example.co.uk which is a local firm offering the same services. This is for your ref only and not to be copied.

Target Market(s)

Property Investors/Landlords

Coding

Coded - Design and coding required

Number of Pages Required

5+ page

Colors
0392cd
f68d4d

Requirements
Must have
• local feel. Possibly using some local architecture or historic landmarks etc. This is fexible.
• most also be mobile device compatible
Nice to have
• the membership logos - files attached: KTB, DWF, GMV and safehold-example.co.uk

```html
<!DOCTYPE html>
<html lang="en">
<head>
<meta charset="utf-8">
<title>Thornbury Lettings Managment Ltd</title>
<link rel="stylesheet" href="https://fonts.googleapis.com/css2?family=Montserrat:wght@400;600;700&family=Open+Sans:wght@400;600&display=swap">
<style>
:root{
  --brand-dark:#1d5d7b;
  --brand-blue:#1c7ab3;
  --brand-orange:#e8962e;
  --topbar:#2a6d8c;
  --text:#555;
  --text-dark:#333;
  --muted:#aaa;
  --line:#5b8aa0;
  --grey-band:#e8e8ea;
  --track:#efefef;
  --btn:#3e3e3e;
  --footer-bottom:#2b2b2b;
  --white:#fff;
}
*{box-sizing:border-box;margin:0;padding:0}
html,body{width:1200px;height:3077px;overflow:hidden}
body{position:relative;background:var(--white);font-family:'Montserrat',sans-serif;color:var(--text)}
.abs{position:absolute}

.top-bar{left:0;top:0;width:1200px;height:41px;background:linear-gradient(#2f7a9b,#1f5a75);color:var(--white);font-size:12px;font-weight:600;padding:12px 0 0 117px}
.site-header{left:0;top:41px;width:1200px;height:123px;background:var(--white)}
.brand{left:164px;top:24px;display:flex;align-items:center;gap:12px}
.brand-mark{width:44px;height:44px;background:var(--brand-dark)}
.brand-name{color:var(--brand-dark);font-weight:700;font-size:20px;line-height:24px;width:240px}
.main-nav{left:665px;top:34px;display:flex;gap:0}
.main-nav a{font-size:15px;font-weight:600;color:var(--brand-dark);text-decoration:none;margin-right:0}
.main-nav a.active{color:var(--brand-orange)}

.hero{left:0;top:164px;width:1200px;height:425px;background:linear-gradient(180deg,#c9d9e6 0%,#b98a6a 35%,#9a6446 62%,#6f7f88 85%,#8fa2ad 100%)}
.hero-title{left:154px;top:320px;font-family:'Open Sans',sans-serif;font-size:56px;color:var(--white);letter-spacing:1px;line-height:60px}
.hero-line{left:146px;font-family:'Open Sans',sans-serif;font-size:22px;color:var(--white);background:rgba(40,40,40,.45);padding:2px 8px;line-height:28px}

.to-top{left:1126px;width:45px;height:32px;background:var(--btn)}
.to-top svg{display:block;margin:9px auto 0}

.service-img{top:664px;width:301px;height:202px;box-shadow:0 6px 8px rgba(0,0,0,.25)}
.service-title{top:886px;font-size:17px;font-weight:700;color:var(--brand-orange)}
.service-text{top:928px;width:301px;font-size:12.4px;line-height:18px;color:var(--text)}
.more-link{font-size:12.4px;color:var(--text-dark);font-weight:600}

.divider{left:109px;width:982px;height:2px;background:var(--line)}
.diamond{width:36px;height:36px;background:#1e6080;transform:rotate(45deg)}

.section-heading{font-size:26px;font-weight:600;color:var(--brand-dark);line-height:46px;letter-spacing:.5px}

.stat{left:109px;width:369px;height:32px;background:var(--track)}
.stat-fill{height:32px;background:var(--brand-blue);color:var(--white);font-size:11.5px;font-weight:700;padding:9px 0 0 14px;white-space:nowrap}
.feature-img{left:519px;top:1477px;width:572px;height:381px;box-shadow:0 6px 8px rgba(0,0,0,.25)}

.quote{left:619px;top:2033px;width:472px;height:139px;background:#f3f1f1;padding:24px 24px;font-size:12.4px;line-height:19px;font-style:italic;color:#777}
.quote-tail{left:648px;top:2171px;width:0;height:0;border-left:10px solid transparent;border-right:10px solid transparent;border-top:12px solid #f3f1f1}
.author{left:622px;top:2190px;display:flex;align-items:center;gap:18px;font-size:12px;color:var(--text-dark)}
.author b{font-weight:700}

.partner-arrow{top:2350px;width:26px;height:26px;background:#9a9a9a}
.partner-arrow svg{display:block;margin:7px auto 0}
.partner-name{left:570px;top:2346px;width:150px;height:36px;border:1px solid #ddd;font-size:13px;font-weight:600;color:var(--brand-blue);text-align:center;line-height:34px}
.partner-badge-a{left:780px;top:2331px;width:50px;height:66px;background:#2a8a9e}
.partner-badge-b{left:899px;top:2311px;width:134px;height:107px;border:1px solid #ddd;background:var(--white)}
.partner-badge-b span{position:absolute;left:18px;top:34px;width:96px;height:38px;background:#7a3d8e}

.footer-band{left:0;top:2506px;width:1200px;height:13px;background:var(--grey-band)}
.footer-col-title{top:2565px;font-size:12px;font-weight:700;color:var(--brand-dark)}
.footer-about{left:111px;top:2678px;width:225px;font-size:12.4px;line-height:19px;color:var(--text)}
.footer-menu{left:361px;top:2600px;width:225px}
.footer-menu a{display:block;height:42px;padding-top:12px;font-size:11.5px;font-weight:600;color:var(--muted);text-decoration:none;border-bottom:2px solid #b9b9b9}
.footer-menu a.active{color:var(--brand-dark)}
.contact-details{left:613px;top:2606px;font-size:12px;line-height:19px;color:var(--text)}
.contact-details .val{color:var(--muted)}
.form-label{left:868px;font-size:12px;color:var(--text-dark)}
.form-field{left:868px;width:224px;height:30px;border:1px solid #c9c9c9;background:var(--white)}
.send-btn{left:868px;top:2934px;width:40px;height:20px;background:var(--brand-orange);color:var(--white);font-size:11px;font-weight:700;text-align:center;line-height:20px}

.bottom-bar{left:0;top:3015px;width:1200px;height:62px;background:var(--footer-bottom);color:#8a8a8a;font-size:11px;padding:24px 0 0 110px}
.social{top:3037px;width:14px;height:14px;border-radius:50%;background:#4e4e4e}
</style>
</head>
<body>

<div class="abs top-bar">Call Us Today! 0117 496 0321 &nbsp;|&nbsp; hello@thornburylettings.example.co.uk</div>

<header class="abs site-header">
  <div class="abs brand">
    <span class="brand-mark"></span>
    <span class="brand-name">Thornbury Lettings Managment Ltd</span>
  </div>
  <nav class="abs main-nav">
    <a class="active" href="#" style="margin-right:65px">HOME</a>
    <a href="#" style="margin-right:62px">ABOUT</a>
    <a href="#" style="margin-right:62px">SERVICES</a>
    <a href="#">CONTACT</a>
  </nav>
</header>

<section class="abs hero" role="img" aria-label="Photograph of red-brick Bristol harbourside buildings beside the river under a blue sky"></section>
<h1 class="abs hero-title">SOLUTIONS</h1>
<div class="abs hero-line" style="top:408px">FOR LANDLORDS</div>
<div class="abs hero-line" style="top:455px">TENANTS &amp; AGENCIES</div>
<div class="abs hero-line" style="top:500px">FIND OUT ABOUT OUR SERVICES</div>

<!-- scroll-to-top buttons -->
<a class="abs to-top" style="top:593px" href="#"><svg width="14" height="10" viewBox="0 0 14 10"><path d="M2 8 L7 3 L12 8" stroke="#fff" stroke-width="2" fill="none"/></svg></a>
<a class="abs to-top" style="top:1003px" href="#"><svg width="14" height="10" viewBox="0 0 14 10"><path d="M2 8 L7 3 L12 8" stroke="#fff" stroke-width="2" fill="none"/></svg></a>
<a class="abs to-top" style="top:1413px" href="#"><svg width="14" height="10" viewBox="0 0 14 10"><path d="M2 8 L7 3 L12 8" stroke="#fff" stroke-width="2" fill="none"/></svg></a>
<a class="abs to-top" style="top:1820px" href="#"><svg width="14" height="10" viewBox="0 0 14 10"><path d="M2 8 L7 3 L12 8" stroke="#fff" stroke-width="2" fill="none"/></svg></a>
<a class="abs to-top" style="top:2228px" href="#"><svg width="14" height="10" viewBox="0 0 14 10"><path d="M2 8 L7 3 L12 8" stroke="#fff" stroke-width="2" fill="none"/></svg></a>
<a class="abs to-top" style="top:2636px" href="#"><svg width="14" height="10" viewBox="0 0 14 10"><path d="M2 8 L7 3 L12 8" stroke="#fff" stroke-width="2" fill="none"/></svg></a>

<!-- services -->
<div class="abs service-img" style="left:109px;background:linear-gradient(160deg,#3f7fc9,#dfe6ec 60%,#8a8f92)" role="img" aria-label="Photograph of modern white apartment block with balconies"></div>
<div class="abs service-img" style="left:449px;background:linear-gradient(180deg,#4e8ad0,#c9d6e2 55%,#6d6a66)" role="img" aria-label="Photograph of new glass office buildings on the harbourside"></div>
<div class="abs service-img" style="left:790px;background:linear-gradient(180deg,#6d9fd8,#e4e0d6 55%,#4a4a48)" role="img" aria-label="Photograph of a curved Georgian terrace with railings"></div>

<h2 class="abs service-title" style="left:109px">LANDLORDS</h2>
<h2 class="abs service-title" style="left:449px">AGENCIES</h2>
<h2 class="abs service-title" style="left:790px">TENANTS</h2>

<div class="abs service-text" style="left:109px">Lid est laborum dolo rumes fugats untras. Etha rums ser quidem rerums facilis dolores nemis onis fugats vitaes nemo minima rerums unsers sadips amets. Ut enim ad minim veniam, quis nostrud neque porro quisquam Ut enim ad minim veniam, quis nostrud Neque porro quisquam est, qui dolorem ipsum quia dolor sit amet, consectetur, adipisci amets uns. Nemo enim ipsam voluptatem quia voluptas sit aspernatur aut odit aut fugit.<br><br><span class="more-link">Find Out More...</span></div>
<div class="abs service-text" style="left:449px">Lid est laborum dolo rumes fugats untras. Etha rums ser quidem rerums facilis dolores nemis onis fugats vitaes nemo minima rerums unsers sadips amets. Ut enim ad minim veniam, quis nostrud neque porro quisquam Ut enim ad minim veniam, quis nostrud Neque porro quisquam est, qui dolorem ipsum quia dolor sit amet, consectetur, adipisci amets uns. Nemo enim ipsam voluptatem quia voluptas sit aspernatur aut odit aut fugit, sed quia consequuntur magni dolores eos qui ratione voluptatem sequi nesciunt. Asunt in anim uis aute irure dolor in reprehenderit in voluptate velit esse cillumsert.<br><br><span class="more-link">Find Out More...</span></div>
<div class="abs service-text" style="left:790px">Lid est laborum dolo rumes fugats untras. Etha rums ser quidem rerums facilis dolores nemis onis fugats vitaes nemo minima rerums unsers sadips amets. Ut enim ad minim veniam, quis nostrud neque porro quisquam Ut enim ad minim veniam, quis nostrud Neque porro quisquam est.<br><br><span class="more-link">Find Out More...</span></div>

<div class="abs divider" style="top:1369px"></div>
<div class="abs diamond" style="left:581px;top:1352px"></div>

<!-- reliability -->
<h2 class="abs section-heading" style="left:109px;top:1476px">WE MANAGE YOUR ESTATE<br>WITH PROVEN RELIABLITY</h2>
<div class="abs stat" style="top:1614px"><div class="stat-fill" style="width:63%">Any kind of statistic goes here 63</div></div>
<div class="abs stat" style="top:1657px"><div class="stat-fill" style="width:95%">Tenant Satisfaction 95</div></div>
<div class="abs stat" style="top:1702px"><div class="stat-fill" style="width:98%">Time Property has sitting tenant 98</div></div>
<div class="abs stat" style="top:1746px"><div class="stat-fill" style="width:35%">Any kind of statistic goes here 35</div></div>
<div class="abs feature-img" style="background:linear-gradient(180deg,#dfe3e6 0%,#c7ccd0 40%,#6f8a5a 65%,#5c6b48 100%)" role="img" aria-label="Photograph of the Clifton suspension bridge over the gorge with hot air balloons"></div>

<div class="abs divider" style="top:1964px"></div>
<div class="abs diamond" style="left:581px;top:1947px"></div>

<!-- testimonial -->
<h2 class="abs section-heading" style="left:109px;top:2047px">OUR SATISFIED CUSTOMERS</h2>
<div class="abs quote">Lid est laborum dolo rumes fugats untras. Etha rums ser quidem rerums facilis dolores nemis onis fugats vitaes nemo minima rerums unsers sadips amets. Ut enim ad minim veniam, quis nostrud neque porro quisquam Ut enim ad minim veniam, quis nostrud Neque porro quisquam est, qui dolorem ipsum quia dolor</div>
<div class="abs quote-tail"></div>
<div class="abs author">
  <svg width="22" height="28" viewBox="0 0 22 28"><circle cx="11" cy="8" r="6" fill="#333"/><path d="M1 26 Q11 10 21 26 Z" fill="#333"/></svg>
  <span><b>Helen Marsh</b>, Landlord</span>
</div>

<div class="abs divider" style="left:207px;width:786px;top:2259px;height:1px"></div>

<!-- partners -->
<h2 class="abs section-heading" style="left:109px;top:2324px">OUR TRUSTED LOCAL<br>CONNECTIONS</h2>
<a class="abs partner-arrow" style="left:518px" href="#"><svg width="8" height="12" viewBox="0 0 8 12"><path d="M6 1 L1 6 L6 11" stroke="#fff" stroke-width="2" fill="none"/></svg></a>
<div class="abs partner-name">safehold-example.co.uk</div>
<div class="abs partner-badge-a"></div>
<div class="abs partner-badge-b"><span></span></div>
<a class="abs partner-arrow" style="left:1065px" href="#"><svg width="8" height="12" viewBox="0 0 8 12"><path d="M2 1 L7 6 L2 11" stroke="#fff" stroke-width="2" fill="none"/></svg></a>

<!-- footer -->
<div class="abs footer-band"></div>
<div class="abs brand" style="left:118px;top:2597px;gap:8px">
  <span class="brand-mark" style="width:30px;height:30px"></span>
  <span class="brand-name" style="font-size:13px;line-height:15px;width:160px">Thornbury Lettings Managment Ltd</span>
</div>
<p class="abs footer-about">Thornbury Lettings Managment Ltd Lorem ipsum ex vix illud nonummy, novum tation et his. At vix scriptaset patrioque scribentur, at pro fugit erts verterem molestiae, sed et vivendo all Lorem ipsum ex vix illud nonummy, novum tation et his. At vix scripta patrioque scribentur...</p>

<h3 class="abs footer-col-title" style="left:361px">MENU</h3>
<nav class="abs footer-menu">
  <a class="active" href="#">HOME</a>
  <a href="#">ABOUT</a>
  <a href="#">SERVICES</a>
  <a href="#">CONTACT</a>
</nav>

<h3 class="abs footer-col-title" style="left:613px">CONTACT DETAILS</h3>
<div class="abs contact-details">
  Phone: 0117 496 0321<br>
  Email: <span class="val">hello@thornburylettings.example.co.uk</span><br>
  Web:<br>
  <span class="val">www.thornburylettings.example.co.uk</span>
</div>

<h3 class="abs footer-col-title" style="left:868px">GET IN TOUCH</h3>
<div class="abs form-label" style="top:2604px">Your Name (required)</div>
<div class="abs form-field" style="top:2624px"></div>
<div class="abs form-label" style="top:2656px">Your Email (required)</div>
<div class="abs form-field" style="top:2675px"></div>
<div class="abs form-label" style="top:2705px">Organisation</div>
<div class="abs form-field" style="top:2724px"></div>
<div class="abs form-label" style="top:2755px">Your Message</div>
<div class="abs form-field" style="top:2774px;height:138px"></div>
<div class="abs send-btn">Send</div>

<div class="abs bottom-bar">Copyright 2016 Thornbury Lettings Managment Ltd | All Rights Reserved</div>
<span class="abs social" style="left:876px"></span>
<span class="abs social" style="left:906px"></span>
<span class="abs social" style="left:936px"></span>
<span class="abs social" style="left:966px"></span>
<span class="abs social" style="left:996px"></span>
<span class="abs social" style="left:1026px"></span>
<span class="abs social" style="left:1056px"></span>

</body>
</html>
```